Ceramic vs. Graphene

Need a one page flyer that discusses the benefits of paint protection and then does a compare and contrast for ceramic vs. graphene coatings. The files have some AI generated ideas and flows. Need to get this to one page and get to the Brisk Loom branding. I've included previous designs done on this site

```html
<!DOCTYPE html>
<html lang="en">
<head>
<meta charset="utf-8">
<title>Ceramic vs. Graphene – Brisk Loom</title>
<link href="https://fonts.googleapis.com/css2?family=Archivo+Black&family=Sora:wght@300;400;500&display=swap" rel="stylesheet">
<style>
:root{
  --sky:#8bbaf5;
  --paper:#ffffff;
  --ink:#1f1f1f;
  --band:#232323;
  --yellow:#ffe600;
  --amber:#e0961e;
  --mist:#f0f0f0;
  --rule:#d9d9d9;
  --white:#ffffff;
}
*{margin:0;padding:0;box-sizing:border-box}
html,body{width:878px;height:1200px;overflow:hidden}
body{background:var(--sky);position:relative;font-family:"Sora",sans-serif;color:var(--ink);letter-spacing:-.025em}
.heavy{font-family:"Archivo Black",sans-serif;font-weight:400;letter-spacing:-.03em;text-transform:uppercase}
.panel{position:absolute;left:65px;width:748px;background:var(--paper);box-shadow:0 10px 24px rgba(0,0,0,.12)}
.panel-top{top:63px;height:529px}
.panel-bottom{top:608px;height:529px;overflow:hidden}

/* title */
.title-tag{position:absolute;left:55px;top:28px;width:263px;height:36px;background:var(--yellow);border-radius:4px;font-size:23px;display:flex;align-items:center;justify-content:center}
.title-main{position:absolute;left:318px;top:25px;width:375px;height:43px;background:var(--ink);color:var(--white);border-radius:4px;font-size:29px;display:flex;align-items:center;justify-content:center}

.intro{position:absolute;left:52px;top:82px;width:360px;font-size:11.8px;line-height:1.2}
.intro p{margin-bottom:9px}
.intro .lead{font-weight:500}
.list{list-style:none;font-weight:300;font-size:11.6px;line-height:16px;padding-left:12px}
.all-coatings{position:absolute;left:413px;top:82px;width:310px;font-size:11.6px}
.all-coatings h2{font-size:12.5px;margin-bottom:5px}
.all-coatings .lead{font-weight:500;margin-bottom:6px}

/* dark band */
.band{position:absolute;left:0;top:229px;width:748px;height:300px;background:var(--band);color:var(--white)}
.brand{position:absolute;left:280px;top:210px;width:188px;height:40px;background:var(--white);border:2px solid var(--yellow);border-radius:5px;display:flex;align-items:center;justify-content:center;font-family:"Archivo Black",sans-serif;font-size:18px;color:var(--ink);z-index:2}
.coat{position:absolute;top:22px;height:270px;font-size:11.4px}
.coat h3{font-size:21px;line-height:19px}
.coat h3 sub{font-size:11px}
.coat .desc{position:absolute;left:0;top:53px;font-weight:300;font-size:11.6px;line-height:13.8px}
.features{position:absolute;left:0;top:102px;display:grid;grid-template-columns:115px 125px;grid-template-rows:50px auto;font-weight:300;font-size:11.4px;line-height:12.8px}
.coat .who{position:absolute;left:0;font-size:11px;line-height:12px;white-space:nowrap}
.ceramic{left:32px;width:250px}
.ceramic .who{top:218px}
.graphene{left:486px;width:262px}
.graphene .desc{width:215px}
.graphene .features{grid-template-columns:127px 120px;grid-template-rows:50px 40px auto}
.graphene .who{top:237px}
.vehicle{position:absolute;left:260px;top:59px;width:208px;height:202px;border-radius:40px 40px 12px 12px;background:linear-gradient(90deg,#9ea3a8,#c9cdd1 48%,#6b6d70 52%,#8d8f92)}
.split{position:absolute;left:363px;top:57px;width:1.5px;height:203px;background:var(--yellow)}

/* bottom */
.key{position:absolute;left:26px;top:27px;font-size:28px;line-height:25px}
.compare{position:absolute;left:26px;top:90px;width:321px;height:197px;table-layout:fixed;border:1px solid var(--rule);border-radius:6px;overflow:hidden;border-collapse:separate;border-spacing:0;font-size:11px;font-weight:300}
.compare th{height:40px;background:var(--amber);color:var(--white);font-family:"Archivo Black",sans-serif;font-weight:400;text-align:left;font-size:12px;line-height:12px;padding:0 0 0 10px;text-transform:uppercase;letter-spacing:-.03em}
.compare td{height:18px;padding:2px 0 1px 10px;border-bottom:1px solid var(--rule);vertical-align:top;line-height:13px;white-space:nowrap}
.compare tr:first-child td{height:23px;padding-top:8px}
.compare tr.tall td{height:31px}
.compare tr:last-child td{border-bottom:none;height:29px}
.note{position:absolute;left:26px;top:297px;width:186px;height:122px;background:var(--yellow);border-radius:4px;padding:16px 12px 0 17px;font-size:11.4px;font-weight:300;line-height:13.8px}
.note h4{font-size:14.5px;line-height:16px;margin-bottom:6px}
.science{position:absolute;left:387px;top:0;width:361px;height:529px;background:var(--mist)}
.topic{position:absolute;left:22px;width:330px}
.topic h3{font-size:19.5px;line-height:19px;margin-bottom:7px}
.topic p{font-size:11.6px;font-weight:300;line-height:13.8px;width:265px}
.topic.wide p{width:280px}
</style>
</head>
<body>

<section class="panel panel-top">
  <div class="title-tag heavy">The Smart Choice</div>
  <div class="title-main heavy">Protect Your Paint</div>

  <div class="intro">
    <p>Your vehicle’s finish takes a beating every day—UV rays, heat, contaminants, and water spots all slowly damage your paint.</p>
    <p class="lead">A professional coating is one of the<br>best investments you can make to</p>
    <ul class="list">
      <li>Preserve your vehicle’s value</li>
      <li>Keep it looking newer, longer</li>
      <li>Reduce maintenance &amp; cleaning time</li>
    </ul>
  </div>

  <div class="all-coatings">
    <h2 class="heavy">What all professional coatings do</h2>
    <p class="lead">Whether you choose Ceramic or Graphene, you get</p>
    <ul class="list">
      <li>Long-term paint protection</li>
      <li>Deep gloss &amp; color enhancement</li>
      <li>Water beading / hydrophobic surface</li>
      <li>Easier cleaning (less dirt sticks)</li>
      <li>UV &amp; oxidation protection</li>
    </ul>
  </div>

  <div class="brand">Brisk Loom</div>

  <div class="band">
    <div class="coat ceramic">
      <h3 class="heavy">Ceramic<br>Coating (SiO<sub>2</sub>)</h3>
      <p class="desc">A hard, glass-like protective layer<br>bonded to your paint.</p>
      <div class="features">
        <span>High-gloss,<br>mirror-like finish</span>
        <span>Excellent protection<br>for daily drivers</span>
        <span>Reliable,<br>time-tested<br>performance</span>
        <span>Strong surface<br>hardness<br>(scratch resistance)</span>
      </div>
      <p class="who heavy">Customers who want<br>great protection and value</p>
    </div>

    <div class="vehicle" role="img" aria-label="Front view of a silver sedan, left half glossy ceramic finish, right half textured graphene finish with a layered crystal block above the hood"></div>
    <div class="split"></div>

    <div class="coat graphene">
      <h3 class="heavy">Graphene Coating<br>(Next-Gen Hybrid)</h3>
      <p class="desc">A reinforced coating using graphene technology for improved flexibility and performance.</p>
      <div class="features">
        <span>More flexible (less<br>micro- cracking<br>over time)</span>
        <span>Better heat<br>dissipation<br>(runs cooler in sun)</span>
        <span>Anti-static<br>(less dust attraction)</span>
        <span>Improved water<br>spot resistance</span>
        <span style="grid-column:1 / 3">Extremely slick surface<br>(stays cleaner longer)</span>
      </div>
      <p class="who heavy">Customers who want maximum<br>performance and lowest maintenance</p>
    </div>
  </div>
</section>

<section class="panel panel-bottom">
  <h2 class="key heavy">Key<br>Differences</h2>

  <table class="compare">
    <colgroup><col style="width:93px"><col style="width:93px"><col></colgroup>
    <thead>
      <tr><th>Feature</th><th>Ceramic<br>Coating</th><th>Graphene<br>Coating</th></tr>
    </thead>
    <tbody>
      <tr><td>Finish</td><td>High-gloss</td><td>Deep, slick gloss</td></tr>
      <tr><td>Durability</td><td>2–5 years</td><td>5–7+ years</td></tr>
      <tr><td>Water Behavior</td><td>Strong beading</td><td>Faster water shedding</td></tr>
      <tr><td>Heat Handling</td><td>Standard</td><td>Improved</td></tr>
      <tr class="tall"><td>Water Spot<br>Resistance</td><td>Moderate</td><td>Better</td></tr>
      <tr><td>Maintenance</td><td>Low</td><td>Lowest</td></tr>
      <tr><td>Investment</td><td>$$</td><td>$$$</td></tr>
    </tbody>
  </table>

  <div class="note">
    <h4 class="heavy">Ceramic ($SiO_2$)</h4>
    <p>Based on sol-gel chemistry, it forms a 3D crystalline lattice that is chemically stable but can be brittle and lacks thermal conductivity.</p>
  </div>

  <div class="science">
    <div class="topic" style="top:56px">
      <h3 class="heavy">Hardness vs. Toughness</h3>
      <p>Ceramics offer high scratch resistance via a rigid lattice, while Graphene adds "tensile toughness," allowing the coating to flex without micro-cracking during thermal expansion.</p>
    </div>
    <div class="topic wide" style="top:157px">
      <h3 class="heavy">Water Contact Angle<br>(The Left Side 100–110)</h3>
      <p>Ceramics have a higher thermal insulator affect which may not dissipate minerals as well. Graphene's higher thermal conductivity helps dissipate heat more thoroughly which reduces mineral etching.</p>
    </div>
    <div class="topic wide" style="top:296px">
      <h3 class="heavy">Visual Aesthetics</h3>
      <p>Ceramic provides a sharp, gloss-like reflection, while Graphene offers a deeper, "wet-look" gloss.</p>
    </div>
  </div>
</section>

</body>
</html>
```